Letter Head Design

I need a letter head design based on my company logo that I attached.
Include phone number: (403)582-4316
Address: 347 14th Avenue NE, Calgary, Alberta, Canada, T3K 4R8

Industry/Entity Type

It Company

```html
<!DOCTYPE html>
<html lang="en">
<head>
<meta charset="utf-8">
<title>BrightNook Interiors Corp. — Letterhead</title>
<link rel="stylesheet" href="https://fonts.googleapis.com/css2?family=Arimo:wght@400;700&family=Open+Sans:wght@400&display=swap">
<style>
  :root {
    --brand-green: #4caf4a;
    --brand-blue: #1670c0;
    --brand-blue-dark: #0d5aa8;
    --ink: #111111;
    --footer-grey: #5a5a5a;
    --paper: #ffffff;
  }
  html, body { margin: 0; padding: 0; overflow: hidden; background: var(--paper); }
  .letterhead {
    position: relative;
    width: 927px;
    height: 1200px;
    overflow: hidden;
    background: var(--paper);
    font-family: "Arimo", Arial, sans-serif;
    color: var(--ink);
  }
  .header-wave, .footer-band { position: absolute; left: 0; display: block; }
  .header-wave { top: 0; }
  .footer-band { bottom: 0; }

  .brand { position: absolute; left: 34px; top: 124px; }
  .brand-mark {
    display: block;
    width: 104px; height: 98px;
    margin-left: 51px;
    background: var(--brand-green);
    border-radius: 4px;
  }
  .brand-name {
    margin: 14px 0 0;
    font-size: 36px;
    font-weight: 400;
    color: var(--brand-blue);
    letter-spacing: -0.5px;
  }

  .letter {
    position: absolute;
    left: 108px; top: 350px;
    width: 725px;
    font-size: 18px;
    line-height: 27.4px;
  }
  .letter p { margin: 0 0 27px; }
  .letter .date { margin-bottom: 31px; }
  .letter .salutation { margin-bottom: 31px; }
  .letter .salutation strong { font-weight: 700; }
  .letter .sign-off { margin-top: 6px; }

  .footer-contact {
    position: absolute;
    left: 64px; top: 1153px;
    font-family: "Open Sans", Arial, sans-serif;
    font-size: 15.5px;
    color: var(--footer-grey);
    margin: 0;
  }
  .footer-contact .sep { margin: 0 6px; }

  .footer-brand {
    position: absolute;
    left: 690px; top: 1128px;
    display: flex; align-items: center; gap: 12px;
  }
  .footer-brand-mark {
    width: 50px; height: 50px;
    border: 3px solid var(--paper);
    box-sizing: border-box;
    border-radius: 3px;
  }
  .footer-brand-name {
    font-size: 30px;
    color: var(--paper);
    font-weight: 400;
    letter-spacing: -0.5px;
  }
</style>
</head>
<body>
<div class="letterhead">

  <svg class="header-wave" width="927" height="400" viewBox="0 0 927 400" aria-hidden="true">
    <path fill="var(--brand-blue)" d="M0,0 L0,82 C220,20 420,150 600,270 C720,350 830,385 927,387 L927,0 Z"/>
    <path fill="var(--paper)" d="M0,0 L0,12 C50,4 95,0 135,0 Z"/>
    <path fill="var(--brand-green)" stroke="var(--paper)" stroke-width="6"
          d="M130,-4 C330,26 460,170 620,250 C730,305 830,322 930,322 L930,-4 Z"/>
  </svg>

  <div class="brand">
    <span class="brand-mark"></span>
    <p class="brand-name">BrightNook</p>
  </div>

  <main class="letter">
    <p class="date">April 16, 2014</p>
    <p class="salutation"><strong>Mr. Daniel Hartley</strong>,</p>
    <p>Lorem ipsum dolor sit amet, consectetur adipiscing elit. Morbi vel ultrices nisl. Ut porttitor accumsan ipsum, quis gravida elit commodo sed. Vivamus pharetra tincidunt mauris. Donec vestibulum mi at diam viverra volutpat. Donec auctor non orci semper porta. Praesent neque erat, tincidunt ut elementum adipiscing, pulvinar eu diam. In hac habitasse platea dictumst. Praesent euismod arcu risus, nec vulputate libero aliquam et. Nam pretium nisi sed orci molestie aliquam. Integer dolor urna, interdum ac ligula a, facilisis interdum lacus.</p>
    <p>Sed sodales non lacus venenatis eleifend. Aliquam erat volutpat. Integer mattis sapien a quam consequat, eu elementum leo tincidunt. Proin in nunc auctor, pellentesque nisl eu, ullamcorper neque. Duis eget euismod ligula. Nunc rhoncus justo ut odio adipiscing malesuada. Vivamus sagittis lacus id velit pharetra molestie. Aliquam placerat sodales purus, vel interdum ipsum faucibus elementum. Class aptent taciti sociosqu ad litora torquent per conubia nostra, per inceptos himenaeos. Curabitur faucibus massa ligula, ut laoreet nulla mattis id. Suspendisse ipsum arcu, pharetra id interdum nec, sagittis non metus.</p>
    <p class="sign-off">Sincerely,<br>Bright Nook | Interiors Corp.</p>
  </main>

  <svg class="footer-band" width="927" height="95" viewBox="0 0 927 95" aria-hidden="true">
    <defs>
      <linearGradient id="footerBlue" x1="0" y1="0" x2="1" y2="1">
        <stop offset="0" stop-color="var(--brand-blue)"/>
        <stop offset="1" stop-color="var(--brand-blue-dark)"/>
      </linearGradient>
    </defs>
    <rect x="0" y="86" width="927" height="9" fill="var(--brand-blue)"/>
    <path fill="url(#footerBlue)" d="M687,2 L927,2 L927,95 L607,95 Z"/>
  </svg>

  <p class="footer-contact">(403)582-4316<span class="sep">|</span>347 14th Avenue NE, Calgary, Alberta, Canada, T3K 4R8</p>

  <div class="footer-brand">
    <span class="footer-brand-mark"></span>
    <span class="footer-brand-name">BrightNook</span>
  </div>

</div>
</body>
</html>
```